The Hollow - Short Film Poster Design

A short film that follows a forest ranger contemplating suicide as he stumbles upon three kids lost in the forest, each in their own, different way.

Genre: Contemporary Dark Drama

Seeking a poster that really stands out as a 'Festival Piece'. See the following lists for references:

QRVN Festival Poster Awards: https://www.snapvault.example/photos/officialqrvn/with/48203917562/

Here is the FULL RESOLUTION short film to take screen grabs and reference photos from:
https://www.filecrate.example/s/kp7wq2rzt91mxe4/Hollow014.mov?oref=e

We are open to much of anything, but this project needs to stand out as unique. On top of that, we are trying to push the angle of strangers LOST in the forest (hence the name) and have thought of the opening sequence of the young man walking through the woods on the epic wide shot of being used for the poster art.

Various items need to be included on the poster: (Please feel free to reword as appropriate)

1) A FILM BY GORDON FAIRWEATHER
2) A DENNIS HOLMGRAVE PRODUCTION

All other taglines are optional and subject to addition or removal.

Please message with all other questions and comments.
Updates

Hey everyone, I apologize for not providing a high enough resolution copy of the short. I was told that this was the highest resolution until I got back straight from my editor who said it's a preliminary. Unfortunately, I do not have the ENTIRE film at top resolution. I will, however, attach high resolution .tiffs from various points of the film for use. https://www.filecrate.example/sh/wte8pqz41nd75ub/BBXKTmcPoLRWqDYe27fhZwNtb?dl=0

Industry/Entity Type

Film Production

Font styles to use
Serif
Sans Serif

Requirements
Must have
• 1) A FILM BY GORDON FAIRWEATHER
• 2) A DENNIS HOLMGRAVE PRODUCTION
• "THE HOLLOW" - Name of Film
Nice to have
• Tagline, but not necessary.

```html
<!DOCTYPE html>
<html lang="en">
<head>
<meta charset="utf-8">
<title>The Hollow — Poster</title>
<link href="https://fonts.googleapis.com/css2?family=Big+Shoulders+Stencil+Display:wght@800&family=Oswald:wght@400&family=Caveat:wght@500&display=swap" rel="stylesheet">
<style>
  :root {
    --ink: #0b0b0b;
    --paper: #f2f2f2;
    --credit: #e6e6e6;
  }
  html, body {
    margin: 0;
    padding: 0;
    width: 800px;
    height: 1200px;
    overflow: hidden;
    background: var(--ink);
  }
  .poster {
    position: relative;
    width: 800px;
    height: 1200px;
    background: var(--ink);
    overflow: hidden;
  }
  .key-art {
    position: absolute;
    top: 0;
    left: 0;
    width: 800px;
    height: 1062px;
    display: block;
  }
  .title-block {
    position: absolute;
    top: 446px;
    left: 0;
    width: 800px;
    text-align: center;
    color: var(--ink);
  }
  .title {
    margin: 0;
    font-family: "Big Shoulders Stencil Display", "Impact", sans-serif;
    font-weight: 800;
    font-size: 76px;
    line-height: 1;
    letter-spacing: 2px;
  }
  .tagline {
    margin: 2px 0 0 0;
    font-family: "Caveat", cursive;
    font-weight: 500;
    font-size: 21px;
    letter-spacing: 2px;
    text-transform: uppercase;
    transform: skewX(-8deg);
  }
  .credits {
    position: absolute;
    top: 1029px;
    left: 0;
    width: 800px;
    margin: 0;
    text-align: center;
    font-family: "Oswald", "Arial Narrow", sans-serif;
    font-size: 10px;
    letter-spacing: .2px;
    color: var(--credit);
  }
  .credits span + span { margin-left: 8px; }
  .cast-strip {
    position: absolute;
    top: 1060px;
    left: 0;
    width: 800px;
    height: 110px;
    display: flex;
    border-top: 2px solid var(--paper);
    border-bottom: 2px solid var(--paper);
  }
  .cast-frame { flex: 1; }
  .cast-frame.one { background: linear-gradient(90deg, #cfcfcf, #8c7a6a 45%, #3a3a3a); }
  .cast-frame.two { background: linear-gradient(90deg, #2a2a2a, #8a7c72 50%, #2c2c2c); }
  .cast-frame.three { background: linear-gradient(90deg, #6a6e66, #5e5448 50%, #1f2024); }
  .cast-frame.four { background: linear-gradient(90deg, #7a5e4a, #9a7258 50%, #3a2e28); }
</style>
</head>
<body>
  <main class="poster">
    <svg class="key-art" viewBox="0 0 800 1062" role="img" aria-label="Grainy black and white double exposure of a face blended with a forest canopy seen from below">
      <defs>
        <filter id="soft" x="-50%" y="-50%" width="200%" height="200%">
          <feGaussianBlur stdDeviation="38"/>
        </filter>
        <filter id="softer" x="-50%" y="-50%" width="200%" height="200%">
          <feGaussianBlur stdDeviation="14"/>
        </filter>
        <filter id="grain">
          <feTurbulence type="fractalNoise" baseFrequency="0.9" numOctaves="2" seed="7"/>
          <feColorMatrix type="matrix" values="0 0 0 0 1  0 0 0 0 1  0 0 0 0 1  0 0 0 -1.6 1.1"/>
        </filter>
        <radialGradient id="vignette" cx="50%" cy="48%" r="62%">
          <stop offset="0" stop-color="#3c3c3c"/>
          <stop offset=".7" stop-color="#1a1a1a"/>
          <stop offset="1" stop-color="#050505"/>
        </radialGradient>
      </defs>
      <rect width="800" height="1062" fill="url(#vignette)"/>
      <g filter="url(#soft)">
        <ellipse cx="420" cy="470" rx="210" ry="150" fill="#d8d8d8"/>
        <ellipse cx="330" cy="330" rx="130" ry="80" fill="#9a9a9a"/>
        <ellipse cx="470" cy="640" rx="110" ry="90" fill="#bdbdbd"/>
        <ellipse cx="90" cy="460" rx="120" ry="60" fill="#a8a8a8"/>
        <ellipse cx="140" cy="790" rx="140" ry="60" fill="#8c8c8c"/>
        <ellipse cx="720" cy="440" rx="70" ry="120" fill="#5a5a5a"/>
        <ellipse cx="260" cy="180" rx="150" ry="60" fill="#4a4a4a"/>
      </g>
      <g filter="url(#softer)">
        <polygon points="470,1062 800,720 800,1062" fill="#8e8e8e"/>
        <polygon points="560,1000 790,770 800,800 600,1010" fill="#c4c4c4"/>
        <ellipse cx="120" cy="600" rx="170" ry="70" fill="#0e0e0e" opacity=".8"/>
        <ellipse cx="640" cy="600" rx="90" ry="140" fill="#0e0e0e" opacity=".6"/>
      </g>
      <rect width="800" height="1062" filter="url(#grain)" opacity=".22"/>
    </svg>

    <div class="title-block">
      <h1 class="title">THE HOLLOW</h1>
      <p class="tagline">Four lifes. One path.</p>
    </div>

    <p class="credits">
      <span>• A FILM BY GORDON FAIRWEATHER</span>
      <span>• A DENNIS HOLMGRAVE PRODUCTION</span>
    </p>

    <div class="cast-strip">
      <div class="cast-frame one" role="img" aria-label="Film still of a young girl in a white knit hat"></div>
      <div class="cast-frame two" role="img" aria-label="Film still of a young woman with long dark hair"></div>
      <div class="cast-frame three" role="img" aria-label="Film still of a young man in a hood among trees"></div>
      <div class="cast-frame four" role="img" aria-label="Film still of a bearded forest ranger in a hat"></div>
    </div>
  </main>
</body>
</html>
```